Automotive Mechanic Website Design

We are working with an auto repair shop in California.
A few websites for inspiration:
https://northbaymotorcraft.com
https://www.portfoliqo.net/gallery/51730486/Velmora-Auto-Services-Repair-SiteKit-Theme
http://www.grindvoltmotors.com
https://www.keelbrant.net
https://www.tvgaragecraft.com
Thank you for taking the time to consider designing a website for us. We are web developers based in Stockton, CA, USA. Most of our projects go through the same process. Understanding this process may help you win a project with us. We custom-code all of our websites in-house. We don’t have any requirements as to what tools you use for your design, but we ask that you follow these guidelines.
IMAGES:
If you use any images or icons in the design, we ask that you have a link to the asset so we can purchase the image/icon. Most of the designs we submit do not have the customer’s images on them unless they have some great images. Be creative; show us the feeling you are trying to portray with your image choices. Use any royalty-free site you choose. We subscribe to Quillo and mainly use their images, but we can purchase images outside of Quillo. PLEASE NOTE: we will not submit designs to clients with watermarks on the images.
FONTS:
We ask that you identify the fonts you’re using in the design. This can be done in a message if you want. We typically use Typora Fonts and Quillo Fonts.
CONTENT:
We're always open to different content and ideas. We often submit designs with stock images so the client can see our vision. We typically take pictures after the website launch to use their images with our vision. Lorem Ipsum is fine for paragraphs, but we ask that you make the Headers with correct English. We want to be able to show the vision and identify the sections of the website.
INSPIRATION:
We typically add a couple of links in the brief of websites we like to help you get started in your design.
REVISIONS:
We do not often ask for revisions of the designs unless we see something in the design that may not appeal to the client. If there are slight changes that we want to make, we do that in the development process.
FEEDBACK:
We rarely give feedback on designs during the design process. We are working on many website projects and do not have the time to provide feedback. We usually respond if your request is well thought out and asks specific questions, but a note asking “feedback, please” usually goes unanswered.

```html
<!DOCTYPE html>
<html lang="en">
<head>
<meta charset="utf-8">
<title>Kestrel Auto Repair</title>
<link href="https://fonts.googleapis.com/css2?family=Audiowide&family=Lexend:wght@300;400;500;600&display=swap" rel="stylesheet">
<style>
:root{
  --red:#e5524a;
  --red-deep:#d9423a;
  --ink:#0b0d1f;
  --navy:#0b0f26;
  --navy-2:#111634;
  --pink:#fdf3f3;
  --grey:#efeff1;
  --text:#3b3d4a;
  --white:#fff;
}
*{margin:0;padding:0;box-sizing:border-box}
html,body{width:1200px;height:4767px;overflow:hidden}
body{position:relative;background:var(--white);font-family:"Lexend",sans-serif;color:var(--text)}
.abs{position:absolute}
.display{font-family:"Audiowide",sans-serif;font-style:italic;color:var(--ink);text-transform:uppercase;letter-spacing:-1px}
.para{font-size:11.5px;line-height:18px;font-weight:300;color:var(--text)}
.para.ruled{border-left:2px solid var(--red);padding-left:16px}
.btn{display:flex;align-items:center;gap:14px;font-size:9px;letter-spacing:1.2px;text-transform:uppercase;font-weight:500;padding-left:30px;clip-path:polygon(0 0,100% 0,92% 100%,0 100%)}
.btn svg{width:12px;height:12px}
.btn.dark{background:var(--ink);color:#fff}
.btn.red{background:var(--red);color:#fff}
.btn.light{background:#fff;color:var(--ink)}
.photo{position:absolute}

.topbar{left:411px;top:0;width:789px;height:33px;background:var(--red);display:flex;align-items:center;justify-content:flex-end;gap:40px;padding-right:150px;color:#fff;font-size:9px}
.topbar span{display:flex;align-items:center;gap:10px}
.topbar i{width:18px;height:18px;border-radius:50%;background:#fff;display:inline-block}
.logo{font-family:"Lexend",sans-serif;font-weight:600;color:var(--red);font-size:30px;letter-spacing:1px;line-height:1}
.logo small{display:block;font-size:15px;color:var(--ink);letter-spacing:.5px;margin-top:4px;text-align:right}
.nav{left:437px;top:56px;width:613px;height:40px;border-bottom:1px solid #d9d9de;display:flex;justify-content:flex-end;gap:74px;font-size:12px;color:var(--ink)}
.nav a{color:inherit;text-decoration:none;position:relative;height:40px}
.nav a.on:after{content:"";position:absolute;left:0;right:0;bottom:-1px;height:2px;background:var(--red)}

.sec-pink{left:0;top:680px;width:1200px;height:682px;background:var(--pink)}
.sec-grey{left:0;top:1362px;width:1200px;height:836px;background:var(--grey)}
.band-red{left:0;top:2920px;width:1200px;height:561px;background:var(--red)}
.footer{left:0;top:4255px;width:1200px;height:512px;background:var(--navy)}

.benefit{left:640px;display:flex;gap:22px;align-items:flex-start}
.benefit .ico{width:52px;height:52px;border-radius:50%;border:1px solid #f1c9c6;display:flex;align-items:center;justify-content:center;flex:none}
.benefit .ico b{width:34px;height:34px;border-radius:50%;background:var(--red);display:block}
.benefit h4{font-size:15px;font-style:italic;font-weight:500;color:var(--ink);margin:8px 0 4px;text-transform:uppercase}
.benefit p{font-size:10px;line-height:15px;font-weight:300;width:280px}

.stats{left:150px;top:3130px;width:355px;height:240px;display:grid;grid-template-columns:1fr 1fr;grid-template-rows:1fr 1fr;color:#fff;text-align:center}
.stats div{display:flex;flex-direction:column;align-items:center;justify-content:center;gap:6px;background:rgba(255,255,255,.04)}
.stats div:nth-child(1),.stats div:nth-child(2){border-bottom:1px solid rgba(255,255,255,.35)}
.stats div:nth-child(1),.stats div:nth-child(3){border-right:1px solid rgba(255,255,255,.35)}
.stats small{font-size:9px;letter-spacing:.6px;line-height:13px;text-transform:uppercase}
.stats strong{font-family:"Audiowide",sans-serif;font-style:italic;font-size:28px;font-weight:400}

.step{position:absolute;width:452px;height:152px;background:linear-gradient(135deg,#4a4f5c,#1b1e28);clip-path:polygon(0 0,100% 0,92% 100%,0 100%)}
.step.r{clip-path:polygon(8% 0,100% 0,100% 100%,0 100%)}
.step span{position:absolute;left:40px;bottom:18px;color:#fff;font-size:15px;font-style:italic;font-weight:500;text-transform:uppercase}
.step.r span{left:70px}

.flink{left:558px;font-size:12px;color:#fff}
.contact-box{left:727px;top:4353px;width:323px;height:295px;background:var(--navy-2)}
.crow{position:absolute;left:50px;display:flex;gap:18px;color:#fff}
.crow svg{width:16px;height:16px;flex:none;margin-top:6px}
.crow small{display:block;font-size:7px;letter-spacing:.8px;color:#aab}
.social{top:4733px;width:20px;height:20px;border-radius:50%;background:#fff}
</style>
</head>
<body>

<div class="abs topbar">
  <span><i></i>000-000-0000</span>
  <span><i></i>info@loremipsum.com</span>
</div>
<div class="abs logo" style="left:150px;top:34px">KESTREL<small>AUTO REPAIR</small></div>
<nav class="abs nav">
  <a class="on" href="#">Home</a><a href="#">Our Services</a><a href="#">Warranty</a><a href="#">Contact Us</a>
</nav>

<svg class="abs" style="left:0;top:96px" width="1200" height="584" viewBox="0 0 1200 584" aria-hidden="true">
  <polygon points="611,0 1200,0 1200,584 540,584" fill="#ececee"/>
</svg>
<div class="photo" role="img" aria-label="Red sports coupe on the road, front three-quarter view" style="left:530px;top:170px;width:670px;height:510px;background:linear-gradient(160deg,#f0f0f2 0%,#d92b2b 35%,#8e1414 60%,#4a4a50 85%);clip-path:polygon(25% 0,100% 0,100% 100%,17% 100%,0 60%)"></div>
<h1 class="abs display" style="left:150px;top:176px;font-size:52px;line-height:64px">Expert<br>Care for<br>Your Car</h1>
<p class="abs para ruled" style="left:150px;top:388px;width:300px;font-size:10.5px">Lorem Ipsum is simply dummy text of the printing and typesetting industry. Lorem Ipsum has been the industry's standard dummy text ever since the 1500s</p>
<div class="abs btn dark" style="left:148px;top:508px;width:210px;height:40px">Schedule Services <svg viewBox="0 0 12 12"><path d="M2 2l4 4-4 4M6 2l4 4-4 4" fill="none" stroke="#fff" stroke-width="1.4"/></svg></div>
<svg class="abs" style="left:625px;top:622px" width="220" height="58" viewBox="0 0 220 58" aria-hidden="true">
  <polygon points="12,0 220,0 208,58 0,58" fill="var(--red)"/>
  <line x1="66" y1="28" x2="154" y2="28" stroke="#1b1b24" stroke-width="1"/>
  <circle cx="66" cy="28" r="5" fill="#1b1b24"/>
  <circle cx="110" cy="28" r="4" fill="none" stroke="#1b1b24"/>
  <circle cx="154" cy="28" r="4" fill="none" stroke="#1b1b24"/>
</svg>

<div class="abs sec-pink"></div>
<div class="photo" role="img" aria-label="Alloy wheel and tyre close-up" style="left:0;top:962px;width:162px;height:253px;background:linear-gradient(135deg,#d7d8dc,#5a5d66 60%,#23252c)"></div>
<div class="photo" role="img" aria-label="Gloved hand polishing a car body with a buffer" style="left:178px;top:785px;width:400px;height:473px;background:linear-gradient(150deg,#c9cacf,#8b8d95 55%,#3e4048)"></div>
<h2 class="abs display" style="left:627px;top:778px;font-size:35px;line-height:44px">Innovative<br>Solutions for<br>Automotive<br>Needs.</h2>
<div class="abs para ruled" style="left:625px;top:978px;width:415px;font-size:10.5px">
  <p>Lorem Ipsum is simply dummy text of the printing and typesetting industry. Lorem Ipsum has been the industry's standard dummy text ever since the 1500s</p>
  <p style="margin-top:18px">when an unknown printer took a galley of type and scrambled it to make a type specimen book. It has survived not only five centuries, but also the leap into electronic typesetting, remaining essentially unchanged. It was popularised in the 1960s with the release of Kordane sheets containing Lorem Ipsum passages, and more recently with desktop publishing software like Verlin PageForge including versions of Lorem Ipsum.</p>
</div>
<div class="abs btn red" style="left:625px;top:1205px;width:165px;height:40px">Learn More <svg viewBox="0 0 12 12"><path d="M2 2l4 4-4 4M6 2l4 4-4 4" fill="none" stroke="#fff" stroke-width="1.4"/></svg></div>

<div class="abs sec-grey"></div>
<h2 class="abs display" style="left:0;top:1462px;width:1200px;text-align:center;font-size:33px;line-height:44px">Precision Maintenance,<br>Service, &amp; Repair</h2>
<p class="abs para" style="left:270px;top:1564px;width:660px;text-align:center;font-size:10.5px">Lorem Ipsum is simply dummy text of the printing and typesetting industry. Lorem Ipsum has been the industry's standard dummy text ever since the 1500s</p>
<svg class="abs" style="left:0;top:1646px" width="1200" height="552" viewBox="0 0 1200 552" aria-hidden="true">
  <polygon points="470,0 1200,0 1200,552 350,552" fill="var(--navy)"/>
</svg>
<div class="photo" role="img" aria-label="Red sports car, front view with service icons around it" style="left:0;top:1710px;width:540px;height:375px;background:linear-gradient(160deg,#f2f2f4 0%,#d42a2a 35%,#7c1212 70%,#26262c);clip-path:polygon(0 10%,70% 0,100% 35%,85% 100%,0 100%)"></div>
<svg class="abs" style="left:160px;top:1690px" width="400" height="380" viewBox="0 0 400 380" aria-hidden="true">
  <g fill="#fff" stroke="#f1c9c6">
    <circle cx="41" cy="41" r="27"/><circle cx="190" cy="112" r="22"/><circle cx="276" cy="130" r="22"/>
    <circle cx="363" cy="218" r="22"/><circle cx="355" cy="330" r="22"/><circle cx="236" cy="356" r="22"/>
  </g>
  <g fill="var(--red)">
    <circle cx="41" cy="41" r="12"/><circle cx="190" cy="112" r="9"/><circle cx="276" cy="130" r="9"/>
    <circle cx="363" cy="218" r="9"/><circle cx="355" cy="330" r="9"/><circle cx="236" cy="356" r="9"/>
  </g>
</svg>
<h3 class="abs display" style="left:622px;top:1752px;font-size:28px;color:#fff">Diagnostics</h3>
<div class="abs para ruled" style="left:620px;top:1805px;width:415px;font-size:10.5px;color:#dfe0ea">
  <p>Lorem Ipsum is simply dummy text of the printing and typesetting industry. Lorem Ipsum has been the industry's standard dummy text ever since the 1500s</p>
  <p style="margin-top:18px">when an unknown printer took a galley of type and scrambled it to make a type specimen book. It has survived not only five centuries, but also the leap into electronic typesetting, remaining essentially unchanged. It was popularised in the 1960s with the release of Kordane sheets containing Lorem Ipsum passages, and more recently with desktop publishing software like Verlin PageForge including versions of Lorem Ipsum.</p>
</div>
<div class="abs btn light" style="left:620px;top:2030px;width:180px;height:40px">Schedule Now <svg viewBox="0 0 12 12"><path d="M2 2l4 4-4 4M6 2l4 4-4 4" fill="none" stroke="#0b0d1f" stroke-width="1.4"/></svg></div>
<div class="abs display" style="left:985px;top:2030px;font-size:80px;color:#141a3c">01</div>
<svg class="abs" style="left:345px;top:2135px" width="170" height="63" viewBox="0 0 170 63" aria-hidden="true">
  <polygon points="12,0 78,0 66,63 0,63" fill="var(--red)"/>
  <polygon points="102,0 168,0 156,63 90,63" fill="var(--red)"/>
  <path d="M42 25l-6 6 6 6M34 25l-6 6 6 6" fill="none" stroke="#fff" stroke-width="2"/>
  <path d="M122 25l6 6-6 6M130 25l6 6-6 6" fill="none" stroke="#fff" stroke-width="2"/>
</svg>

<div class="photo" role="img" aria-label="Mechanic with clipboard inspecting an engine bay" style="left:150px;top:2302px;width:440px;height:514px;background:linear-gradient(160deg,#dcdde0,#7b7e86 45%,#1e2027)"></div>
<h2 class="abs display" style="left:645px;top:2312px;font-size:33px;line-height:44px">Experience the<br>Advantages of<br>Excellence</h2>
<div class="abs benefit" style="top:2488px"><div class="ico"><b></b></div><div><h4>We Make It Easy</h4><p>Lorem Ipsum is simply dummy text of the printing and typesetting industry.</p></div></div>
<div class="abs benefit" style="top:2574px"><div class="ico"><b></b></div><div><h4>Fair and Transparent Pricing</h4><p>Lorem Ipsum is simply dummy text of the printing and typesetting industry.</p></div></div>
<div class="abs benefit" style="top:2661px"><div class="ico"><b></b></div><div><h4>OEM Factory Parts Warranty</h4><p>Lorem Ipsum is simply dummy text of the printing and typesetting industry.</p></div></div>
<div class="abs benefit" style="top:2752px"><div class="ico"><b></b></div><div><h4>Satisfaction Guaranteed</h4><p>Lorem Ipsum is simply dummy text of the printing and typesetting industry.</p></div></div>

<div class="abs band-red"></div>
<div class="photo" role="img" aria-label="Hands tightening an engine part with a wrench" style="left:550px;top:2998px;width:650px;height:550px;background:linear-gradient(140deg,#c7a14a,#6b5a3c 40%,#2c2e34 80%);clip-path:polygon(18% 0,100% 0,100% 100%,0 100%)"></div>
<h2 class="abs display" style="left:150px;top:3010px;font-size:33px;line-height:44px;color:#fff">Experience That<br>Builds Trust</h2>
<div class="abs stats">
  <div><small>Years in<br>Business</small><strong>40</strong></div>
  <div><small>Vehicles<br>Repaired</small><strong>40K</strong></div>
  <div><strong>10</strong><small>Technicians &amp;<br>Advisors</small></div>
  <div><strong>100%</strong><small>Satisfied<br>Customers</small></div>
</div>

<div class="step" role="img" aria-label="Technician working under a raised car" style="left:150px;top:3652px"><span>Choose Your Service</span></div>
<h2 class="abs display" style="left:657px;top:3660px;font-size:33px;line-height:44px">Let Us Show<br>You How It's<br>Done</h2>
<div class="step" role="img" aria-label="Customer and mechanic hands with thumbs up and wrench" style="left:150px;top:3820px"><span>Make an Appointment</span></div>
<div class="step r" role="img" aria-label="Vehicle on a lift in a repair shop" style="left:598px;top:3820px"><span>Drop Off Vehicle for Service</span></div>
<p class="abs para ruled" style="left:150px;top:4012px;width:410px;font-size:10.5px">Lorem Ipsum is simply dummy text of the printing and typesetting industry. Lorem Ipsum has been the industry's standard dummy text ever since the 1500s</p>
<div class="abs btn dark" style="left:148px;top:4098px;width:210px;height:40px">Schedule Services <svg viewBox="0 0 12 12"><path d="M2 2l4 4-4 4M6 2l4 4-4 4" fill="none" stroke="#fff" stroke-width="1.4"/></svg></div>
<div class="step r" role="img" aria-label="Customer receiving car keys at the counter" style="left:598px;top:4000px;background:linear-gradient(135deg,#3a4a66,#b0672a 70%,#2a2d36)"><span>Pick Up Your Car Keys</span></div>

<div class="abs footer"></div>
<div class="abs logo" style="left:152px;top:4370px;color:#fff;font-size:44px">KESTREL<small style="color:#fff;font-size:22px">AUTO REPAIR</small></div>
<h4 class="abs display" style="left:150px;top:4525px;font-size:18px;color:#fff">Get Direction</h4>
<div class="abs" style="left:152px;top:4583px;width:320px;height:40px;background:#fff;font-size:9px;letter-spacing:1px;color:#555;padding:16px 0 0 30px">ENTER ADDRESS</div>
<svg class="abs" style="left:425px;top:4583px" width="50" height="40" viewBox="0 0 50 40" aria-hidden="true">
  <polygon points="8,0 50,0 42,40 0,40" fill="var(--red)"/>
  <path d="M20 16l4 4-4 4M25 16l4 4-4 4" fill="none" stroke="#fff" stroke-width="1.4"/>
</svg>
<h4 class="abs display" style="left:558px;top:4358px;font-size:18px;color:#fff">Links</h4>
<div class="abs flink" style="top:4408px">Home</div>
<div class="abs flink" style="top:4465px">Our Services</div>
<div class="abs flink" style="top:4522px">Warranty</div>
<div class="abs flink" style="top:4580px">Contact Us</div>
<div class="abs contact-box">
  <h4 class="display" style="position:absolute;left:50px;top:28px;font-size:18px;color:#fff">Contact</h4>
  <div class="crow" style="top:80px"><svg viewBox="0 0 16 16"><rect x="1" y="3" width="14" height="10" fill="#fff"/><path d="M1 3l7 6 7-6" fill="none" stroke="#111634"/></svg><div><small>MAIL</small><span style="font-size:12px">info@loremipsum.com</span></div></div>
  <div class="crow" style="top:142px"><svg viewBox="0 0 16 16"><path d="M15 1L1 7l6 2 2 6z" fill="#fff"/></svg><div><small>ADDRESS</small><span style="font-size:10px;line-height:12px;display:block">2290 W LARKSPUR RD, MERCED,<br>CA 95340 LIC #417733</span></div></div>
  <div class="crow" style="top:215px"><svg viewBox="0 0 16 16"><path d="M4 1l3 3-2 2c1 2 3 4 5 5l2-2 3 3-2 3C7 15 1 9 1 3z" fill="#fff"/></svg><div><small>PHONE</small><span style="font-size:16px">000-000-0000</span></div></div>
</div>
<div class="abs" style="left:150px;top:4737px;font-size:10px;color:#fff">© Copyright © 2023 kestrel. All rights reserved.</div>
<div class="abs social" style="left:932px"></div>
<div class="abs social" style="left:965px"></div>
<div class="abs social" style="left:997px"></div>
<div class="abs social" style="left:1030px"></div>
<svg class="abs" style="left:1125px;top:4690px" width="52" height="50" viewBox="0 0 52 50" aria-hidden="true">
  <polygon points="8,0 52,0 44,50 0,50" fill="var(--red)"/>
  <path d="M21 24l5-5 5 5M21 30l5-5 5 5" fill="none" stroke="#fff" stroke-width="1.6"/>
</svg>

</body>
</html>
```